Holistic Health Coach needs simple web site design for a new practice

I need a web (re)design for my entire site, TR Maple Sprout. I have a beautiful new blue and green logo that I'd like the site fonts and color scheme to be built around. I'll attach my new logo so you'll know the colors/design feel I'm after.

I want easy navigation for my mostly text based site, widgets for my social media pages and a clean, fun, light feel for the site.

Target Market(s)

People looking to take charge of their own health, and who may need my coaching services to obtain optimal wellness.

Industry/Entity Type

Health

Coding

Number of Pages Required

Font styles to use
Script

Colors
33b8a4
33a6d7
ffffff

Requirements
Must have
• Must incorporate my logo design, as well as same/similar fonts and color scheme.
• I'd like it to stay as close to the current design as possible.
Nice to have
• Would love to incorporate a hover over menu (for example, when a user hovers over "About", they will see the submenu in a floating design.
Should not have
• No dark colors or masculine feel

```html
<!DOCTYPE html>
<html lang="en">
<head>
<meta charset="utf-8">
<title>TR Maple Sprout</title>
<link href="https://fonts.googleapis.com/css2?family=Oswald:wght@400;500&family=Roboto:wght@400;500;700&display=swap" rel="stylesheet">
<style>
:root{
  --blue:#2f8cd6;
  --blue-btn:#3c8fe0;
  --green:#8bc553;
  --teal:#33b8a4;
  --ink:#222;
  --text:#444;
  --line:#e3e3e3;
  --page:#ececec;
  --card:#fff;
  --footer-light:#f1f1f1;
  --footer-dark:#1c1c1c;
}
*{box-sizing:border-box;margin:0;padding:0}
html,body{width:1200px;height:2889px;overflow:hidden}
body{font-family:"Roboto",Arial,sans-serif;color:var(--text);background:var(--page);position:relative}
a{color:inherit;text-decoration:none}

/* Header */
.site-header{position:absolute;left:0;top:0;width:1200px;height:164px;background:#fff}
.brand{position:absolute;top:28px;left:0;width:1200px;text-align:center;font-weight:500;font-size:34px;color:var(--teal);letter-spacing:1px}
.main-nav{position:absolute;top:112px;left:108px;width:1000px;height:20px;font-size:16px;color:var(--ink)}
.main-nav a{position:absolute;top:0;white-space:nowrap}
.main-nav .n1{left:0}
.main-nav .n2{left:122px;color:var(--blue)}
.main-nav .n3{left:292px}
.main-nav .n4{left:444px}
.main-nav .n5{left:652px}
.submenu{position:absolute;left:200px;top:164px;width:155px;height:131px;background:#e7e7e7;z-index:3;padding:13px 0 0 28px;font-size:15px;color:#333;line-height:27px;white-space:nowrap}

/* Hero */
.hero{position:absolute;left:0;top:164px;width:1200px;height:539px;background:linear-gradient(100deg,#4a3a36 0%,#6b5a55 35%,#9c8a84 55%,#c9c3c5 80%,#e9e8ec 100%)}
.hero-title{position:absolute;left:121px;top:172px;font-family:"Oswald",sans-serif;color:#fff;white-space:nowrap}
.hero-title h1{font-size:56px;font-weight:400;line-height:64px}
.hero-title p{font-size:36px;line-height:46px}
.hero-arrow{position:absolute;top:224px;width:38px;height:38px;border-radius:50%;background:#fff}
.hero-arrow svg{display:block}
.hero-arrow.prev{left:33px}
.hero-arrow.next{left:1129px}

/* Posts */
.post{position:absolute;left:104px;width:611px;height:418px;background:var(--card);box-shadow:0 1px 3px rgba(0,0,0,.18)}
.post-image{position:absolute;left:10px;top:10px;width:591px;height:202px}
.post-date{position:absolute;left:10px;top:10px;width:58px;height:62px;background:#000;color:#fff;text-align:right;padding:4px 4px 0 0;font-size:11px;line-height:13px}
.post-date .day{display:block;font-size:20px;line-height:22px;text-align:center;margin-left:4px}
.post-date .yr{display:block;font-size:10px;text-align:center;margin-left:4px}
.post-title{position:absolute;left:20px;top:248px;font-size:15px;color:var(--blue);font-weight:400;text-transform:uppercase;letter-spacing:.2px;white-space:nowrap}
.post-excerpt{position:absolute;left:20px;top:276px;width:560px;font-size:12px;line-height:20px;color:#333}
.post-meta{position:absolute;left:16px;top:346px;font-size:12px;color:#222;white-space:nowrap}
.post-share{position:absolute;left:0;top:376px;width:611px;height:42px;border-top:1px solid var(--line);display:flex;justify-content:flex-end;align-items:center;padding-right:24px;gap:30px}
.share{display:flex;align-items:center;gap:4px;font-size:11px}
.share .btn{height:18px;padding:0 6px 0 4px;border:1px solid #bbb;border-radius:2px;display:flex;align-items:center;gap:4px;font-weight:700;color:#335}
.share .btn i{display:block;width:9px;height:9px;background:currentColor;border-radius:2px}
.share .btn.like{background:#4a64a0;color:#fff;border-color:#4a64a0}
.share .btn.plus{color:#c33}
.share .count{border:1px solid #bbb;height:18px;min-width:16px;line-height:16px;text-align:center;border-radius:2px;color:#333}

/* Sidebar */
.widget{position:absolute;left:761px;width:337px;background:var(--card);box-shadow:0 1px 3px rgba(0,0,0,.18)}
.search{top:761px;height:90px;padding:28px 22px;display:flex;gap:12px}
.search .field{width:192px;height:36px;background:#e9e9e9;border:1px solid #ddd;font-size:12px;font-style:italic;color:#888;padding:11px 10px}
.search .go{width:96px;height:36px;background:var(--blue-btn);color:#fff;font-size:14px;text-align:center;line-height:36px;border-radius:2px}
.popular{top:867px;height:570px;padding:22px 28px 0}
.popular h3{font-size:19px;font-weight:500;color:#2a4d8a;margin-bottom:22px}
.pop-item{display:flex;gap:14px;height:100px;border-bottom:1px solid #eee;padding-top:2px}
.pop-item:last-child{border-bottom:0}
.pop-thumb{width:94px;height:72px;border:3px solid #fff;box-shadow:0 1px 4px rgba(0,0,0,.35);flex:none}
.pop-item h4{font-size:13px;font-weight:400;color:#1f4fa0;margin-bottom:4px}
.pop-item p{font-size:11px;line-height:18px;color:#444;width:165px}
.list-widget .head{height:48px;background:var(--green);color:#fff;font-size:21px;font-weight:500;padding:12px 0 0 36px;letter-spacing:.3px}
.list-widget ul{list-style:none;padding:14px 0 0 36px}
.list-widget li{display:flex;align-items:center;gap:12px;height:40px;font-size:15px;color:#333}
.archives{top:1449px;height:390px}
.categories{top:1853px;height:352px}
.promo{top:2219px;height:289px;padding:22px 44px}
.promo-box{width:249px;height:246px;background:#ececec;text-align:center;padding-top:10px}
.promo-box .ask{font-size:16px;line-height:19px;color:#333;font-weight:500}
.promo-box .ask b{font-weight:700;color:#111}
.promo-art{display:flex;justify-content:center;gap:8px;margin:8px 0 4px}
.promo-art .pack{width:128px;height:74px;background:linear-gradient(90deg,#4a6fa8,#8a5aa0,#d8a040)}
.promo-art .seal{width:70px;height:70px;border-radius:50%;background:var(--teal)}
.promo-box .help{font-size:17px;font-style:italic;color:#222}
.promo-box .cta{display:inline-block;margin-top:4px;background:#f07a1a;color:#fff;font-weight:700;font-size:14px;padding:6px 14px;border-radius:3px}

/* Footer */
.footer-links{position:absolute;left:0;top:2567px;width:1200px;height:183px;background:var(--footer-light);border-top:1px solid #ddd}
.f-col{position:absolute;top:30px}
.f-col h5{font-size:17px;font-weight:400;color:var(--blue);margin-bottom:18px}
.f-col li{list-style:none;font-size:11.5px;line-height:24px;color:#222;white-space:nowrap}
.footer-bottom{position:absolute;left:0;top:2750px;width:1200px;height:139px;background:var(--footer-dark);color:#ddd;font-size:13px}
.legal{position:absolute;left:104px;top:40px;line-height:29px}
.social{position:absolute;left:860px;top:44px;display:flex;gap:19px}
.social span{width:42px;height:42px;border-radius:50%;border:3px solid #fff;background:#2a5a9e}
.social .tw{background:#2c9ed8}
.social .gp{background:#c8423a}
.social .li{background:#2a76b0}
</style>
</head>
<body>

<header class="site-header">
  <div class="brand">TR Maple Sprout</div>
  <nav class="main-nav">
    <a class="n1" href="#">HOME</a>
    <a class="n2" href="#">ABOUT TESSA</a>
    <a class="n3" href="#">ARTICLES</a>
    <a class="n4" href="#">ESSENTIAL OILS</a>
    <a class="n5" href="#">21-DAY SWEET RESET COACHING SERVICES</a>
  </nav>
</header>
<div class="submenu">SUB MENU 1<br>SUB MENU 2<br>SUB MENU 3<br>SUB MENU 4</div>

<section class="hero" role="img" aria-label="Photo of a woman in a white knit hat and scarf in a snowy winter setting">
  <div class="hero-title">
    <h1>TR MAPLE SPROUT</h1>
    <p>IPSUM IS SIMPLY DUMMY</p>
  </div>
  <span class="hero-arrow prev"><svg width="38" height="38" viewBox="0 0 38 38"><path d="M21 12l-7 7 7 7" fill="none" stroke="#222" stroke-width="3"/></svg></span>
  <span class="hero-arrow next"><svg width="38" height="38" viewBox="0 0 38 38"><path d="M17 12l7 7-7 7" fill="none" stroke="#222" stroke-width="3"/></svg></span>
</section>

<!-- Blog posts -->
<article class="post" style="top:761px">
  <div class="post-image" role="img" aria-label="Photo of a woman sitting by the sea with wind-blown hair" style="background:linear-gradient(180deg,#dfe6e6 0%,#8fb3ad 45%,#5f8c86 75%,#9a9590 100%)"></div>
  <div class="post-date">Dec<span class="day">20</span><span class="yr">2015</span></div>
  <h2 class="post-title">Lifestyles of the tired and wired</h2>
  <p class="post-excerpt">Lorem Ipsum has been the industry's standard dummy text ever since the 1500s, when an unknown printer took a galley of type and scrambled it to make a type specimen book. It has survived not only</p>
  <p class="post-meta">This entry was posted in Werkstæt on 11/01/2015.</p>
  <div class="post-share">
    <span class="share"><span class="btn"><i></i>Tweet</span><span class="count">0</span></span>
    <span class="share"><span class="btn like"><i></i>Like</span><span class="count">0</span></span>
    <span class="share"><span class="btn plus">+1</span><span class="count">0</span></span>
  </div>
</article>

<article class="post" style="top:1204px">
  <div class="post-image" role="img" aria-label="Photo of a group of smiling young friends in sunglasses" style="background:linear-gradient(180deg,#e9ecef 0%,#b9a79a 40%,#6d7a92 75%,#3a4560 100%)"></div>
  <div class="post-date">Dec<span class="day">20</span><span class="yr">2015</span></div>
  <h2 class="post-title">April Essential Living Education Series</h2>
  <p class="post-excerpt">Lorem Ipsum has been the industry's standard dummy text ever since the 1500s, when an unknown printer took a galley of type and scrambled it to make a type specimen book. It has survived not only</p>
  <p class="post-meta">This entry was posted in Werkstæt on 11/01/2015.</p>
  <div class="post-share">
    <span class="share"><span class="btn"><i></i>Tweet</span><span class="count">0</span></span>
    <span class="share"><span class="btn like"><i></i>Like</span><span class="count">0</span></span>
    <span class="share"><span class="btn plus">+1</span><span class="count">0</span></span>
  </div>
</article>

<article class="post" style="top:1647px">
  <div class="post-image" role="img" aria-label="Photo of a group of students standing together outdoors" style="background:linear-gradient(180deg,#cfe0ee 0%,#9fbfd6 30%,#6f7d5e 65%,#3f4b3a 100%)"></div>
  <div class="post-date">Dec<span class="day">20</span><span class="yr">2015</span></div>
  <h2 class="post-title">Module 3: A nice supplement to the program</h2>
  <p class="post-excerpt">Lorem Ipsum has been the industry's standard dummy text ever since the 1500s, when an unknown printer took a galley of type and scrambled it to make a type specimen book. It has survived not only</p>
  <p class="post-meta">This entry was posted in Werkstatt and tagged overland, Trail Cruiser on 06/01/2015.</p>
  <div class="post-share">
    <span class="share"><span class="btn"><i></i>Tweet</span><span class="count">0</span></span>
    <span class="share"><span class="btn like"><i></i>Like</span><span class="count">0</span></span>
    <span class="share"><span class="btn plus">+1</span><span class="count">0</span></span>
  </div>
</article>

<article class="post" style="top:2090px">
  <div class="post-image" role="img" aria-label="Photo of a smiling student in front of library bookshelves" style="background:linear-gradient(90deg,#d9a64a 0%,#c98a3a 35%,#8a6a4e 60%,#5a4a3c 100%)"></div>
  <div class="post-date">Dec<span class="day">20</span><span class="yr">2015</span></div>
  <h2 class="post-title">Module 3: A nice supplement to the program</h2>
  <p class="post-excerpt">Lorem Ipsum has been the industry's standard dummy text ever since the 1500s, when an unknown printer took a galley of type and scrambled it to make a type specimen book. It has survived not only</p>
  <p class="post-meta">This entry was posted in Werkstatt and tagged overland, Trail Cruiser on 06/01/2015.</p>
  <div class="post-share">
    <span class="share"><span class="btn"><i></i>Tweet</span><span class="count">0</span></span>
    <span class="share"><span class="btn like"><i></i>Like</span><span class="count">0</span></span>
    <span class="share"><span class="btn plus">+1</span><span class="count">0</span></span>
  </div>
</article>

<!-- Sidebar -->
<aside>
  <div class="widget search">
    <div class="field">Search</div>
    <div class="go">Search</div>
  </div>

  <div class="widget popular">
    <h3>POPULAR BLOGS</h3>
    <div class="pop-item"><div class="pop-thumb" role="img" aria-label="Thumbnail photo of a woman" style="background:linear-gradient(135deg,#e8c9bc,#b07a6a)"></div><div><h4>This is a sample Post 1</h4><p>Lorem ipsum dolor sit amet, consectetuer adipiscing elit, sed diam nonummy nibh...</p></div></div>
    <div class="pop-item"><div class="pop-thumb" role="img" aria-label="Thumbnail photo of a desk with papers" style="background:linear-gradient(135deg,#dfe3ea,#6a7590)"></div><div><h4>This is a sample Post 1</h4><p>Lorem ipsum dolor sit amet, consectetuer adipiscing elit, sed diam nonummy nibh...</p></div></div>
    <div class="pop-item"><div class="pop-thumb" role="img" aria-label="Thumbnail photo of a couple" style="background:linear-gradient(135deg,#cfe2f0,#c79a80)"></div><div><h4>This is a sample Post 1</h4><p>Lorem ipsum dolor sit amet, consectetuer adipiscing elit, sed diam nonummy nibh...</p></div></div>
    <div class="pop-item"><div class="pop-thumb" role="img" aria-label="Thumbnail photo of a woman" style="background:linear-gradient(135deg,#e4d6d0,#4a3a3a)"></div><div><h4>This is a sample Post 1</h4><p>Lorem ipsum dolor sit amet, consectetuer adipiscing elit, sed diam nonummy nibh...</p></div></div>
    <div class="pop-item"><div class="pop-thumb" role="img" aria-label="Thumbnail photo of a woman" style="background:linear-gradient(135deg,#efe0cc,#a0704a)"></div><div><h4>This is a sample Post 1</h4><p>Lorem ipsum dolor sit amet, consectetuer adipiscing elit, sed diam nonummy nibh...</p></div></div>
  </div>

  <div class="widget list-widget archives">
    <div class="head">ARCHIVES</div>
    <ul>
      <li><svg width="14" height="12" viewBox="0 0 14 12"><path d="M1 1l5 5-5 5M7 1l5 5-5 5" fill="none" stroke="#2f6fc0" stroke-width="1.6"/></svg>April 2015</li>
      <li><svg width="14" height="12" viewBox="0 0 14 12"><path d="M1 1l5 5-5 5M7 1l5 5-5 5" fill="none" stroke="#2f6fc0" stroke-width="1.6"/></svg>March 2015</li>
      <li><svg width="14" height="12" viewBox="0 0 14 12"><path d="M1 1l5 5-5 5M7 1l5 5-5 5" fill="none" stroke="#2f6fc0" stroke-width="1.6"/></svg>February 2015</li>
      <li><svg width="14" height="12" viewBox="0 0 14 12"><path d="M1 1l5 5-5 5M7 1l5 5-5 5" fill="none" stroke="#2f6fc0" stroke-width="1.6"/></svg>January 2015</li>
      <li><svg width="14" height="12" viewBox="0 0 14 12"><path d="M1 1l5 5-5 5M7 1l5 5-5 5" fill="none" stroke="#2f6fc0" stroke-width="1.6"/></svg>September 2014</li>
      <li><svg width="14" height="12" viewBox="0 0 14 12"><path d="M1 1l5 5-5 5M7 1l5 5-5 5" fill="none" stroke="#2f6fc0" stroke-width="1.6"/></svg>June 2014</li>
      <li><svg width="14" height="12" viewBox="0 0 14 12"><path d="M1 1l5 5-5 5M7 1l5 5-5 5" fill="none" stroke="#2f6fc0" stroke-width="1.6"/></svg>May 2014</li>
      <li><svg width="14" height="12" viewBox="0 0 14 12"><path d="M1 1l5 5-5 5M7 1l5 5-5 5" fill="none" stroke="#2f6fc0" stroke-width="1.6"/></svg>April 2014</li>
    </ul>
  </div>

  <div class="widget list-widget categories">
    <div class="head">CATEGORIES</div>
    <ul>
      <li><svg width="14" height="12" viewBox="0 0 14 12"><path d="M1 1l5 5-5 5M7 1l5 5-5 5" fill="none" stroke="#2f6fc0" stroke-width="1.6"/></svg>21 Day Sweet Reset</li>
      <li><svg width="14" height="12" viewBox="0 0 14 12"><path d="M1 1l5 5-5 5M7 1l5 5-5 5" fill="none" stroke="#2f6fc0" stroke-width="1.6"/></svg>Adrenal Fatigue</li>
      <li><svg width="14" height="12" viewBox="0 0 14 12"><path d="M1 1l5 5-5 5M7 1l5 5-5 5" fill="none" stroke="#2f6fc0" stroke-width="1.6"/></svg>Articles</li>
      <li><svg width="14" height="12" viewBox="0 0 14 12"><path d="M1 1l5 5-5 5M7 1l5 5-5 5" fill="none" stroke="#2f6fc0" stroke-width="1.6"/></svg>DIY</li>
      <li><svg width="14" height="12" viewBox="0 0 14 12"><path d="M1 1l5 5-5 5M7 1l5 5-5 5" fill="none" stroke="#2f6fc0" stroke-width="1.6"/></svg>Essential Oils</li>
      <li><svg width="14" height="12" viewBox="0 0 14 12"><path d="M1 1l5 5-5 5M7 1l5 5-5 5" fill="none" stroke="#2f6fc0" stroke-width="1.6"/></svg>Real Food</li>
      <li><svg width="14" height="12" viewBox="0 0 14 12"><path d="M1 1l5 5-5 5M7 1l5 5-5 5" fill="none" stroke="#2f6fc0" stroke-width="1.6"/></svg>Uncategorized</li>
    </ul>
  </div>

  <div class="widget promo">
    <div class="promo-box">
      <p class="ask">NEED <b>EXTRA SUPPORT</b><br>TO <b><i>ROCK</i></b> YOUR<br><b>21-DAY SWEET RESET?</b></p>
      <div class="promo-art">
        <div class="pack" role="img" aria-label="Program book covers"></div>
        <div class="seal"></div>
      </div>
      <p class="help">I'm here to help</p>
      <span class="cta">TELL ME MORE!</span>
    </div>
  </div>
</aside>

<!-- Footer -->
<footer>
  <div class="footer-links">
    <div class="f-col" style="left:123px"><h5>How We Help</h5><ul><li>Lead Generation</li><li>Tactics Management</li><li>Start-Up Website</li><li>Website Facelifts</li></ul></div>
    <div class="f-col" style="left:403px"><h5>Services</h5><ul><li>Social Media Coaching</li><li>Website Analysis</li><li>Modula Website Design</li><li>Newsletters</li></ul></div>
    <div class="f-col" style="left:682px"><h5>Results</h5><ul><li>Testimonials</li><li>B2B Companies</li><li>Contractors &amp; Construction</li><li>Manufacturing</li></ul></div>
    <div class="f-col" style="left:936px"><h5>Support</h5><ul><li>Why Choose Brightpath</li><li>Our Culture</li><li>Our Team</li><li>Sitemap</li></ul></div>
  </div>
  <div class="footer-bottom">
    <p class="legal">Privacy Policy | Terms of Use | About Us | Sitemap<br>Copyright © 2015 All rights reserved.</p>
    <div class="social">
      <span class="fb" aria-label="Social profile"></span>
      <span class="tw" aria-label="Social profile"></span>
      <span class="gp" aria-label="Social profile"></span>
      <span class="li" aria-label="Social profile"></span>
    </div>
  </div>
</footer>

</body>
</html>
```